BRELM - Letterhead

Willowmere Institute of Letters and Crafts (BRELM) is a non-profit organization that operates two tuition-free public schools - BRELM Elementary for grades K to 5th and BRELM College Prep for grades 6-12.

We are looking for a letterhead primarily to be used on Google Docs and Microsoft Word. Attached are two versions of our logo. One with our name spelled out and one with the acronym.

For Letterhead, we would like 3 addresses listed:

BRELM HQ
41872 Hollow Brook Lane, Suite 308
Fernhollow, CA 90418

BRELM Elementary (K-5)
18460 Marsh Ridge Boulevard
Fernhollow, CA 90418

BRELM College Prep (6-12)
27314 Del Sol Terrace
Cedar Vale Crossing, CA 90426

Our Phone Number is (555) 418-7062
Our Fax Number is the same (555) 418-7062

Our website is www.brelmschools.org

Target Market(s)

Education

Industry/Entity Type

Education

Font styles to use
Sans Serif

Colors
0054AA
0677BA
7BADD7
CADEEF
E8F1F8

Requirements
Must have
• Logo, Address, Phone Number, Website.
Nice to have
• Modern and clean design.
Should not have
• Prefer that there is no bleed -- the letterhead will mostly be used in PDF format however sometimes it will be printed and our printers can not do a full bleed

```html
<!DOCTYPE html>
<html lang="en">
<head>
<meta charset="utf-8">
<title>BRELM Letterhead</title>
<link rel="stylesheet" href="https://fonts.googleapis.com/css2?family=Open+Sans:wght@300;400;600;700&family=Roboto:wght@300;400&display=swap">
<style>
  :root {
    --brand-navy: #1d3f8f;
    --band-blue: #3a56a0;
    --text-grey: #555555;
    --text-dark: #222222;
    --rule-grey: #c4c4c4;
    --accent-red: #e2472c;
    --accent-yellow: #e9b31c;
    --accent-green: #2f9a48;
    --page-bg: #f1f1f1;
    --canvas-bg: #e4e4e4;
  }
  * { margin: 0; padding: 0; box-sizing: border-box; }
  html, body { width: 1200px; height: 1200px; overflow: hidden; background: var(--canvas-bg); }
  .letterhead {
    position: absolute; left: 180px; top: 6px;
    width: 840px; height: 1188px;
    background: var(--page-bg);
    box-shadow: 0 2px 8px rgba(0,0,0,0.12);
    overflow: hidden;
  }
  .brand { position: absolute; left: 61px; top: 50px; display: flex; align-items: center; gap: 10px; }
  .brand-mark { width: 16px; height: 16px; background: var(--brand-navy); flex: none; }
  .brand-name {
    font-family: "Open Sans", sans-serif; font-weight: 700; font-size: 18px;
    line-height: 23px; color: var(--brand-navy); width: 290px;
  }
  .contact-list {
    position: absolute; left: 61px; top: 236px; list-style: none;
    font-family: "Roboto", sans-serif; font-weight: 300; font-size: 13.2px;
    line-height: 17px; color: var(--text-grey);
  }
  .contact-list li { display: flex; align-items: center; gap: 6px; }
  .contact-list svg { width: 11px; height: 11px; fill: var(--brand-navy); }
  .campus {
    position: absolute; left: 61px; font-style: normal;
    font-family: "Roboto", sans-serif; font-weight: 300; font-size: 13.2px;
    line-height: 17px; color: var(--text-grey);
  }
  .campus::before {
    content: ""; display: block; width: 35px; height: 2px;
    background: var(--accent); margin-bottom: 19px;
  }
  .campus--prep { top: 369px; --accent: var(--accent-red); }
  .campus--elem { top: 478px; --accent: var(--accent-yellow); }
  .campus--hq { top: 591px; --accent: var(--accent-green); }
  .column-rule {
    position: absolute; left: 283px; top: 235px; width: 1px; height: 623px;
    background: var(--rule-grey);
  }
  .letter-body {
    position: absolute; left: 311px; top: 228px; width: 469px;
    font-family: "Open Sans", sans-serif; font-weight: 300; font-size: 14px;
    line-height: 19.8px; color: var(--text-grey); text-align: justify;
  }
  .letter-body p { margin-bottom: 19.5px; }
  .letter-body .salutation { text-align: left; }
  .letter-body strong { font-weight: 600; color: var(--text-dark); }
  .signature {
    position: absolute; left: 311px; top: 886px; width: 163px; height: 76px;
    background: linear-gradient(90deg, #dcdcdc, #e9e9e9);
  }
  .footer-band {
    position: absolute; left: 0; bottom: 0; width: 100%; height: 14px;
    background: var(--band-blue);
  }
</style>
</head>
<body>
<main class="letterhead">
  <header class="brand">
    <span class="brand-mark"></span>
    <span class="brand-name">Willowmere Institute of Letters and Crafts</span>
  </header>

  <ul class="contact-list">
    <li><svg viewBox="0 0 24 24"><path d="M6.6 10.8a15 15 0 0 0 6.6 6.6l2.2-2.2a1 1 0 0 1 1-.25 11.4 11.4 0 0 0 3.6.57 1 1 0 0 1 1 1V20a1 1 0 0 1-1 1A17 17 0 0 1 3 4a1 1 0 0 1 1-1h3.5a1 1 0 0 1 1 1c0 1.25.2 2.45.57 3.57a1 1 0 0 1-.25 1z"/></svg>(555) 418-7062</li>
    <li><svg viewBox="0 0 24 24"><path d="M6 2h12v5H6zM4 8h16a2 2 0 0 1 2 2v6h-4v6H6v-6H2v-6a2 2 0 0 1 2-2zm4 8v4h8v-4z"/></svg>(555) 418-7062</li>
    <li><svg viewBox="0 0 24 24"><path d="M12 2a10 10 0 1 0 0 20 10 10 0 0 0 0-20zm6.9 9h-3a15 15 0 0 0-1.3-5.6A8 8 0 0 1 18.9 11zM12 4.1c.9 1.3 1.8 3.7 1.9 6.9h-3.8c.1-3.2 1-5.6 1.9-6.9zM9.4 5.4A15 15 0 0 0 8.1 11h-3a8 8 0 0 1 4.3-5.6zM5.1 13h3a15 15 0 0 0 1.3 5.6A8 8 0 0 1 5.1 13zm6.9 6.9c-.9-1.3-1.8-3.7-1.9-6.9h3.8c-.1 3.2-1 5.6-1.9 6.9zm2.6-1.3a15 15 0 0 0 1.3-5.6h3a8 8 0 0 1-4.3 5.6z"/></svg>www.brelmschools.org</li>
  </ul>

  <address class="campus campus--prep">BRELM College Prep (6-12)<br>27314 Del Sol Terrace<br>Cedar Vale Crossing, CA 90426</address>
  <address class="campus campus--elem">BRELM Elementary (K-5)<br>18460 Marsh Ridge Boulevard<br>Fernhollow, CA 90418</address>
  <address class="campus campus--hq">BRELM HQ<br>41872 Hollow Brook Lane, Suite 308<br>Fernhollow, CA 90418</address>

  <div class="column-rule"></div>

  <article class="letter-body">
    <p class="salutation">Dear Dana Whitfield,</p>
    <p>Lorem ipsum dolor sit amet, consectetuer adipiscing elit, sed diam nonummy nibh euismod tincidunt ut laoreet dolore magna aliquam erat volutpat. Ut wisi enim ad minim veniam, quis nostrud exerci tation ullamcorper suscipit lobortis nisl ut aliquip ex ea commodo consequat. Duis dolore te feugait nulla facilisi. Nam liber tempor cum soluta nobis eleifend option congue nihil imperdiet doming id quod mazim placerat facer possim assum.</p>
    <p><strong>Lorem ipsum dolor sit amet, consectetuer adipiscing elit, sed diam nonummy nibh euismod tincidunt ut laoreet dolore magna aliquam erat volutpat.</strong></p>
    <p>Ut wisi enim ad minim veniam, quis nostrud exerci tation ullamcorper suscipit lobortis nisl ut aliquip ex ea commodo consequat. Consectetuer adipiscing elit, sed diam nonummy nibh euismod tincidunt ut laoreet dolore magna aliquam erat volutpat. Ut wisi enim ad minim veniam, quis nostrud exerci tation ullamcorper suscipit lobortis nisl ut aliquip ex ea commodo consequat. Consectetuer adipiscing elit, sed diam nonummy nibh euismod tincidunt ut laoreet dolore magna aliquam erat volutpat. Ut wisi enim ad minim veniam, quis nostrud.</p>
    <p><strong>Exerci tation ullamcorper suscipit lobortis nisl ut aliquip ex ea commodo consequat.</strong> Consectetuer adipiscing elit, sed diam nonummy nibh euismod tincidunt ut laoreet dolore magna aliquam erat volutpat. Ut wisi enim ad minim veniam, quis nostrud exerci tation ullamcorper suscipit lobortis nisl ut aliquip ex ea commodo consequat. Consectetuer adipiscing elit, sed diam nonummy nibh euismod tincidunt ut laoreet dolore magna aliquam erat volutpat. Ut wisi enim ad minim veniam, quis nostrud exerci tation ullamcorper suscipit lobortis nisl ut aliquip ex ea commodo consequat.</p>
  </article>

  <div class="signature" role="img" aria-label="Handwritten signature of the sender"></div>

  <div class="footer-band"></div>
</main>
</body>
</html>
```